Maple Harbor Home Care Business Cards

We are looking to create double sided, sleek business cards for our new Home Health Care Agency, Maple Harbor Home Care, located in NJ. We want to appear established, professional and at the same time, stand out with a creative and original flair. It should have a luxurious, exclusive feel to it.
The theme colors from our logo should be incorporated into the project.

Our Logo is attached.

Information to be included on the business cards:

Insert Phone Icon: (555)-403-2297
Insert Website Icon: mhhcxq.example
Insert E-mail Icon: info@mhhcxq.example

Follow us on Social Media!
Insert Facebook Icon: (I will provide the link at a later time)
Insert Instagram Icon (I will provide the link at a later time)

In regard to location, we service the areas of: Bayville
Beachwood
Brick
Deal
Howell
Island Heights
Jackson
Lakehurst
Lakewood
Manchester Township
Point Pleasant Beach
Roosevelt
Long Branch
Toms River

All all it's neighboring areas.

However, that can take up a lot of room...therefore, I had in mind to use the backside of the card to have a MAP with all these areas marked on there...in addition to listing these service locations below the map.

We want the card to appear lively and vibrant.

Please note: I will provide the potential winner with the contact's name later on in the process.

A sample idea is attached below as well.

Use your creative juices!

Good luck!

• A map of our service areas on the back of the double sided card.
Sleek design
Our logo (refer to attachment below)

```html
<!DOCTYPE html>
<html lang="en">
<head>
<meta charset="utf-8">
<title>Maple Harbor Home Care – Business Cards</title>
<link href="https://fonts.googleapis.com/css2?family=Montserrat:wght@400;700&display=swap" rel="stylesheet">
<style>
  :root {
    --page: #dcdcdc;
    --navy: #0a4e91;
    --lime: #8bc53f;
    --white: #ffffff;
  }
  * { margin: 0; padding: 0; box-sizing: border-box; }
  html, body { width: 1200px; height: 1200px; overflow: hidden; }
  body { background: var(--page); font-family: 'Montserrat', sans-serif; position: relative; }

  .card { position: absolute; left: 207px; width: 786px; height: 449px; border-radius: 20px; overflow: hidden; }
  .card--front { top: 112px; background: var(--navy); }
  .card--back { top: 640px; background: var(--lime); }

  .brand { position: absolute; text-align: center; color: var(--white); font-weight: 700; }
  .brand__mark { display: block; margin: 0 auto 16px; width: 110px; height: 110px; border-radius: 50%; }
  .brand__name { font-size: 27px; line-height: 1.2; letter-spacing: 0.5px; }
  .card--front .brand { left: 58px; top: 120px; width: 314px; }
  .card--front .brand__mark { background: var(--lime); }
  .card--back .brand { left: 50px; top: 110px; width: 350px; }
  .card--back .brand__mark { background: var(--white); width: 130px; height: 130px; }
  .card--back .brand__name { font-size: 30px; }

  .divider { position: absolute; left: 418px; top: 123px; width: 2px; height: 205px; background: var(--lime); }

  .contact { position: absolute; left: 459px; top: 118px; color: var(--white); }
  .contact__name { font-size: 30px; font-weight: 700; color: var(--lime); letter-spacing: 1.5px; line-height: 1.1; }
  .contact__role { font-size: 20px; margin-top: 2px; }
  .contact__list { list-style: none; margin-top: 20px; }
  .contact__list li { display: flex; align-items: center; font-size: 20px; height: 26px; }
  .contact__list li.gap { margin-top: 13px; }
  .contact__icon { width: 16px; height: 16px; margin-right: 9px; flex: none; }
  .dot { width: 15px; height: 15px; border-radius: 50%; background: var(--lime); margin-right: 10px; flex: none; }

  .areas { position: absolute; left: 448px; top: 36px; list-style: none; color: var(--white); }
  .areas li { display: flex; align-items: center; font-size: 23px; height: 29.2px; }
  .areas li::before { content: ""; width: 15px; height: 15px; border-radius: 50%; background: var(--navy); margin-right: 15px; }
</style>
</head>
<body>

<section class="card card--front">
  <div class="brand">
    <span class="brand__mark"></span>
    <p class="brand__name">MAPLE HARBOR<br>HOME CARE</p>
  </div>

  <div class="divider"></div>

  <div class="contact">
    <h1 class="contact__name">DANIEL REYES</h1>
    <p class="contact__role">Director</p>
    <ul class="contact__list">
      <li><span class="dot"></span>@Icon: mhhcxq.example</li>
      <li><span class="dot"></span>/Icon: mhhcxq.example</li>
      <li class="gap">
        <svg class="contact__icon" viewBox="0 0 16 16"><path d="M3 1 L6 1 L7 5 L5 6.5 C6 9 7.5 10.5 9.5 11 L11 9 L15 10 L15 13 C15 14 14 15 13 15 C6.5 15 1 9.5 1 3 C1 2 2 1 3 1 Z" fill="none" stroke="var(--lime)" stroke-width="1.4"/></svg>
        555-403-2297
      </li>
      <li>
        <svg class="contact__icon" viewBox="0 0 16 16"><rect x="1" y="3" width="14" height="10" fill="none" stroke="var(--lime)" stroke-width="1.4"/><path d="M1 3 L8 9 L15 3" fill="none" stroke="var(--lime)" stroke-width="1.4"/></svg>
        Icon: info@mhhcxq.example
      </li>
      <li>
        <svg class="contact__icon" viewBox="0 0 16 16"><circle cx="8" cy="8" r="7" fill="none" stroke="var(--lime)" stroke-width="1.2"/><ellipse cx="8" cy="8" rx="3" ry="7" fill="none" stroke="var(--lime)" stroke-width="1.2"/><path d="M1 8 H15 M2.5 4.5 H13.5 M2.5 11.5 H13.5" stroke="var(--lime)" stroke-width="1.2"/></svg>
        www.Icon: mhhcxq.example
      </li>
    </ul>
  </div>
</section>

<section class="card card--back">
  <div class="brand">
    <span class="brand__mark"></span>
    <p class="brand__name">MAPLE HARBOR<br>HOME CARE</p>
  </div>

  <ul class="areas">
    <li>Beachwood</li>
    <li>Brick</li>
    <li>Deal</li>
    <li>Howell</li>
    <li>Island Heights</li>
    <li>Jackson</li>
    <li>Lakehurst</li>
    <li>Lakewood</li>
    <li>Manchester Township</li>
    <li>Point Pleasant Beach</li>
    <li>Roosevelt</li>
    <li>Long Branch</li>
    <li>Toms River</li>
  </ul>
</section>

</body>
</html>
```